Layout Existing Logo for Social Media Platforms

Can you create a Twitter, Linkdn and Facebook banner/logo image for a Facebook business page using my same logo and design? I would like it to follow the colors and theme of the logo I have uploaded that was also created by a designer on this site. Of course I am open to suggestions but logo recognition is key. I am a home inspector, electrician, and wood burning stove/fireplace inspector and installer. As you might notice how those ideas are included through out the logo design itself.

Target Market(s)

Real Estate agents, home owners, contractors.

Industry/Entity Type

Home Inspection

Font styles to use
Sans Serif

Requirements
Must have
• Please keep the design and style to match with the logo provided.

```html
<!DOCTYPE html>
<html lang="en">
<head>
<meta charset="utf-8">
<title>Northgate Inspection – Cover Banner</title>
<link rel="stylesheet" href="https://fonts.googleapis.com/css2?family=Oswald:wght@300;400;500&display=swap">
<style>
  :root {
    --page-bg: #e9ebf0;
    --brand-red: #e3202f;
    --brand-red-deep: #c4121f;
    --ink-dark: #1c2029;
    --slate: #3b4654;
    --white: #ffffff;
    --silver-top: #ffffff;
    --silver-bottom: #c9cbcf;
  }
  html, body {
    margin: 0;
    width: 1200px;
    height: 753px;
    overflow: hidden;
    background: var(--page-bg);
  }
  .cover {
    position: absolute;
    left: 0;
    top: 155px;
    width: 1200px;
    height: 442px;
    display: block;
  }
  .cover text {
    font-family: "Oswald", sans-serif;
  }
  .headline-trades { fill: var(--brand-red); font-size: 29px; font-weight: 400; }
  .headline-main { fill: var(--white); font-size: 44px; font-weight: 400; letter-spacing: 0.5px; }
  .tagline { fill: var(--white); font-size: 13.5px; font-weight: 400; letter-spacing: 0.6px; }
  .contact-line { fill: var(--white); font-size: 28px; font-weight: 400; letter-spacing: 0.5px; }
  .brand-name { fill: var(--brand-red); font-size: 17px; font-weight: 500; letter-spacing: 1px; }
  .photo-frame { stroke: var(--brand-red); stroke-width: 5; }
  .photo-edge { fill: none; stroke: #000; stroke-width: 9; }
</style>
</head>
<body>
<svg class="cover" viewBox="0 0 1162 428" xmlns="http://www.w3.org/2000/svg">
  <defs>
    <linearGradient id="houseTone" x1="0" y1="0" x2="1" y2="1">
      <stop offset="0" stop-color="#2b3340"/>
      <stop offset="1" stop-color="#4a5563"/>
    </linearGradient>
    <linearGradient id="photoWarm" x1="0" y1="0" x2="1" y2="1">
      <stop offset="0" stop-color="#d9c9a8"/>
      <stop offset="1" stop-color="#8a7b6a"/>
    </linearGradient>
    <linearGradient id="photoFire" x1="0" y1="0" x2="1" y2="1">
      <stop offset="0" stop-color="#4a3a30"/>
      <stop offset="1" stop-color="#c87a2e"/>
    </linearGradient>
    <linearGradient id="photoLab" x1="0" y1="0" x2="1" y2="1">
      <stop offset="0" stop-color="#2a2f38"/>
      <stop offset="1" stop-color="#6b7480"/>
    </linearGradient>
    <linearGradient id="photoPanel" x1="0" y1="0" x2="1" y2="1">
      <stop offset="0" stop-color="#e8ecef"/>
      <stop offset="1" stop-color="#7d8f9e"/>
    </linearGradient>
    <linearGradient id="silverTab" x1="0" y1="0" x2="0" y2="1">
      <stop offset="0" stop-color="var(--silver-top)"/>
      <stop offset="1" stop-color="var(--silver-bottom)"/>
    </linearGradient>
    <clipPath id="coverClip"><rect width="1162" height="428"/></clipPath>
  </defs>

  <g clip-path="url(#coverClip)">
    <rect class="house-backdrop" width="1162" height="428" fill="url(#houseTone)"
          role="img" aria-label="Photo of a house at dusk seen through a magnifying glass"/>

    <g class="photo-mosaic">
      <polygon class="photo-edge" points="30,220 140,330 30,440 -80,330"/>
      <polygon class="photo-frame" points="30,220 140,330 30,440 -80,330" fill="url(#photoWarm)"
               role="img" aria-label="Photo of an inspector measuring on a roof"/>

      <polygon class="photo-edge" points="230,-90 430,110 230,310 30,110"/>
      <polygon class="photo-frame" points="230,-90 430,110 230,310 30,110" fill="url(#photoWarm)"
               role="img" aria-label="Photo of an inspector in a hard hat checking siding"/>

      <polygon class="photo-edge" points="410,45 560,195 410,345 260,195"/>
      <polygon class="photo-frame" points="410,45 560,195 410,345 260,195" fill="url(#photoFire)"
               role="img" aria-label="Photo of technicians inspecting a fireplace"/>

      <polygon class="photo-edge" points="265,190 410,335 265,480 120,335"/>
      <polygon class="photo-frame" points="265,190 410,335 265,480 120,335" fill="url(#photoLab)"
               role="img" aria-label="Photo of an electrician testing equipment with a meter"/>

      <polygon class="photo-edge" points="570,200 720,350 570,500 420,350"/>
      <polygon class="photo-frame" points="570,200 720,350 570,500 420,350" fill="url(#photoPanel)"
               role="img" aria-label="Photo of an electrician working on a breaker panel"/>
    </g>

    <polygon class="accent-white" points="500,428 1162,198 1162,428" fill="var(--white)"/>
    <polygon class="accent-red" points="560,428 1162,226 1162,428" fill="var(--brand-red)"/>

    <polygon class="brand-tab" points="1000,0 1162,0 1162,95 1000,140" fill="url(#silverTab)"/>
    <rect class="brand-mark" x="1073" y="22" width="16" height="16" fill="var(--brand-red)"/>
    <text class="brand-name" x="1081" y="62" text-anchor="middle">NORTHGATE</text>
    <text class="brand-name" x="1081" y="82" text-anchor="middle">INSPECTION</text>

    <text class="headline-trades" x="764" y="88" text-anchor="middle" textLength="342" lengthAdjust="spacingAndGlyphs">HOME INSPECTOR I ELECTRICIAN</text>
    <text class="headline-main" x="764" y="142" text-anchor="middle" textLength="372" lengthAdjust="spacingAndGlyphs">FIREPLACE INSPECTOR</text>

    <text class="tagline" x="1135" y="341" text-anchor="end">SIMPLY DUMMY TEXT OF THE PRINTING AND</text>
    <text class="tagline" x="1135" y="358" text-anchor="end">TYPESETTING INDUSTRY. LOREM IPSUM HAS</text>

    <text class="contact-line" x="708" y="412" textLength="439" lengthAdjust="spacingAndGlyphs">CALL 012-555-0148 | WWW.NORTHGATE.COM</text>
  </g>
</svg>
</body>
</html>
```